Upcoming lecture sponsored by a church on an important topic

We have a Reformation The Speech coming up at the end of October on the topic of law and gospel. I thought it might be cool to use a flyer that looks like it was from that day and age. Picture what Conrad Velmer would advertise things on kind of an old church/reformation type format. It will be sponsored by our church, and we have a paragraph or two to describe the lecture that would be included on the flyer. We would also want it formatted so that it could be printed on postcards and mailed to churches and individuals.

The flyer should have the following paragraph...

The distinction between the law and the gospel is the most important distinction in the Christian faith. Conrad Velmer: “Distinguishing between the law and the gospel is the highest art in Christendom, one who every person who values the name Christian ought to recognize, know, and possess.” The distinction between the law and the gospel is of great comfort for the child of God. “For the law was given by Moses, but grace and truth came by Jesus Christ” (John 1:17). For these reasons, the distinction between the law and the gospel is the most heavily assaulted doctrine in the Christian faith. This Reformation Day, join us for an explanation and defense of the great distinction between God’s good law and God’s glorious gospel.

And the flyer should have the following information...

Topic: The Steady Word and the Bright Promise
Date and Time: Tuesday, October 31, 2023 at 7:30pm
Host: Harrow Creek Fellowship Church
Speaker: Rev. Gerald Voskuil
Venue: The Marlow Hall, 5172 Brenton Avenue, Hudsonville, MI 49318
Format: Lecture followed by Q&A and refreshments

00AB8E
00BBA5
67D7C9
C6EFE9
E9F9F6

• The color scheme that I would like to have is a teal color (the same color as found at www.brackenhollowchapel.com

```html
<!DOCTYPE html>
<html lang="en">
<head>
<meta charset="utf-8">
<title>The Steady Word and the Bright Promise — Lecture Flyer</title>
<link rel="stylesheet" href="https://fonts.googleapis.com/css2?family=Libre+Caslon+Text:wght@400;700&family=Oswald:wght@600&family=Poppins:wght@400;500;700;800&display=swap">
<style>
  :root {
    --ink: #050505;
    --teal: #3fc1cf;
    --teal-deep: #1f97a6;
    --teal-light: #67d7c9;
    --gold: #f5cf45;
    --gold-pale: #fbf0b4;
    --white: #ffffff;
  }
  * { box-sizing: border-box; margin: 0; padding: 0; }
  html, body { width: 865px; height: 1200px; overflow: hidden; background: var(--ink); }
  .flyer {
    position: relative; width: 865px; height: 1200px; overflow: hidden;
    background: radial-gradient(ellipse at 50% 40%, #1c1c1c 0%, var(--ink) 70%);
    font-family: "Poppins", sans-serif; color: var(--white);
  }
  .cathedral-photo {
    position: absolute; left: 52px; top: 300px; width: 760px; height: 445px;
    background:
      radial-gradient(ellipse 22% 55% at 50% 50%, #d8d8d8 0%, #7a7a7a 35%, rgba(40,40,40,0) 75%),
      radial-gradient(ellipse 60% 70% at 50% 45%, #3a3a3a 0%, #151515 60%, rgba(5,5,5,0) 100%);
  }
  .brand {
    position: absolute; top: 78px; left: 0; width: 100%;
    display: flex; justify-content: center; align-items: center; gap: 12px;
  }
  .brand-mark { width: 14px; height: 14px; background: var(--white); }
  .brand-name {
    font-family: "Libre Caslon Text", serif; font-weight: 400;
    font-size: 34px; letter-spacing: 1px; color: var(--white);
  }
  .title {
    position: absolute; top: 205px; left: 0; width: 100%; text-align: center;
    font-family: "Libre Caslon Text", serif; font-weight: 700; line-height: 1;
  }
  .title-top { display: block; font-size: 45px; color: var(--teal); letter-spacing: 0.5px; }
  .title-main {
    display: block; margin-top: 10px; font-size: 72px;
    background: linear-gradient(90deg, var(--gold) 0%, var(--gold-pale) 50%, var(--gold) 100%);
    -webkit-background-clip: text; background-clip: text; color: transparent;
  }
  .date-ribbon { position: absolute; left: 55px; top: 745px; width: 758px; height: 64px; }
  .date-ribbon svg { position: absolute; inset: 0; }
  .date-text {
    position: absolute; inset: 0; display: flex; align-items: center; justify-content: center;
    font-family: "Oswald", sans-serif; font-weight: 600; font-size: 46px;
    color: var(--white); letter-spacing: -0.5px; white-space: nowrap;
    transform: scaleX(0.88);
  }
  .roles { position: absolute; left: 59px; top: 826px; width: 342px; }
  .role {
    display: flex; height: 30px; margin-bottom: 11px;
    border: 1px solid var(--gold); border-radius: 6px; overflow: hidden;
  }
  .role-label {
    background: var(--gold); color: var(--ink); font-weight: 700; font-size: 18px;
    padding: 0 9px; display: flex; align-items: center;
  }
  .role-value {
    background: var(--ink); flex: 1; font-size: 15.5px; padding: 0 10px 0 8px;
    display: flex; align-items: center; white-space: nowrap;
  }
  .column-rule { position: absolute; left: 429px; width: 1px; background: var(--white); opacity: .8; }
  .venue { position: absolute; left: 444px; top: 822px; width: 380px; }
  .venue-label { color: var(--teal); font-weight: 700; font-size: 19px; line-height: 1.2; }
  .venue-address { font-weight: 700; font-size: 16.5px; line-height: 1.38; }
  .hr { position: absolute; left: 59px; width: 752px; height: 2px;
    background: linear-gradient(90deg, rgba(63,193,207,0) 0%, var(--teal-deep) 15%, var(--teal-deep) 85%, rgba(63,193,207,0) 100%); }
  .format {
    position: absolute; top: 917px; left: 0; width: 100%; text-align: center;
    font-weight: 800; font-size: 25px; color: var(--gold); letter-spacing: 0.2px;
  }
  .point { position: absolute; top: 966px; font-size: 11.5px; line-height: 1.4; }
  .point-left { left: 59px; width: 355px; }
  .point-right { left: 444px; width: 360px; }
  .point-lead { color: var(--teal); font-weight: 700; font-size: 12px; line-height: 1.3; margin-bottom: 6px; }
  .quote-icon { display: inline-block; width: 20px; height: 13px; vertical-align: -1px; margin-right: 4px; }
  .quote-icon.close { margin: 0 0 0 6px; transform: rotate(180deg); vertical-align: -5px; }
  .citation { color: var(--teal); font-weight: 700; font-size: 10.5px; }
  .summary {
    position: absolute; top: 1113px; left: 60px; width: 745px; text-align: center;
    font-size: 10px; line-height: 1.4;
  }
  .website {
    position: absolute; top: 1150px; left: 0; width: 100%; text-align: center;
    font-weight: 700; font-size: 13.5px; letter-spacing: 3.6px; color: var(--white);
  }
  .website-domain { color: var(--gold); }
</style>
</head>
<body>
<main class="flyer">
  <div class="cathedral-photo" role="img" aria-label="Black and white photograph of a Gothic cathedral nave with tall columns and a lit altar"></div>

  <header class="brand">
    <span class="brand-mark"></span>
    <span class="brand-name">BRACKEN HOLLOW CHAPEL</span>
  </header>

  <h1 class="title">
    <span class="title-top">THE STEADY WORD AND THE</span>
    <span class="title-main">BRIGHT PROMISE</span>
  </h1>

  <div class="date-ribbon">
    <svg viewBox="0 0 758 64" width="758" height="64" aria-hidden="true">
      <defs>
        <linearGradient id="ribbonFill" x1="0" y1="0" x2="0" y2="1">
          <stop offset="0" stop-color="#5fd2dd"/>
          <stop offset="1" stop-color="#2aa6b4"/>
        </linearGradient>
      </defs>
      <polygon points="0,0 758,0 730,32 758,64 0,64 28,32" fill="url(#ribbonFill)"/>
      <polyline points="4,0 30,32 4,64" fill="none" stroke="#f5cf45" stroke-width="4"/>
      <polyline points="754,0 728,32 754,64" fill="none" stroke="#f5cf45" stroke-width="4"/>
    </svg>
    <div class="date-text">TUESDAY, OCTOBER 31, 2023 AT 7:30PM</div>
  </div>

  <section class="roles">
    <div class="role"><span class="role-label">Host</span><span class="role-value">Harrow Creek Fellowship Church</span></div>
    <div class="role"><span class="role-label">Speaker</span><span class="role-value">Rev. Gerald Voskuil</span></div>
  </section>

  <div class="column-rule" style="top:826px;height:80px"></div>

  <section class="venue">
    <div class="venue-label">Venue</div>
    <div class="venue-address">The Marlow Hall, 5172 Brenton<br>Avenue, Hudsonville, MI 49318</div>
  </section>

  <div class="hr" style="top:911px"></div>
  <div class="format">LECTURE FOLLOWED BY Q&amp;A AND REFRESHMENTS</div>
  <div class="hr" style="top:957px"></div>

  <section class="point point-left">
    <p class="point-lead">The distinction between the law and the gospel is the most important distinction in the Christian faith. Conrad Velmer:</p>
    <p><svg class="quote-icon" viewBox="0 0 20 13" aria-hidden="true"><g fill="#3fc1cf"><circle cx="4.5" cy="8.5" r="4.5"/><path d="M0.5 8 Q0.5 1 7.5 0 L7.5 2.2 Q3.5 3 3.5 7 Z"/><circle cx="15" cy="8.5" r="4.5"/><path d="M11 8 Q11 1 18 0 L18 2.2 Q14 3 14 7 Z"/></g></svg>Distinguishing between the law and the gospel is the highest art in Christendom, one who every person who values the name Christian ought to recognize, know, and possess<svg class="quote-icon close" viewBox="0 0 20 13" aria-hidden="true"><g fill="#3fc1cf"><circle cx="4.5" cy="8.5" r="4.5"/><path d="M0.5 8 Q0.5 1 7.5 0 L7.5 2.2 Q3.5 3 3.5 7 Z"/><circle cx="15" cy="8.5" r="4.5"/><path d="M11 8 Q11 1 18 0 L18 2.2 Q14 3 14 7 Z"/></g></svg></p>
  </section>

  <div class="column-rule" style="top:966px;height:120px"></div>

  <section class="point point-right">
    <p class="point-lead">The distinction between the law and the gospel is of great comfort for the child of God</p>
    <p><svg class="quote-icon" viewBox="0 0 20 13" aria-hidden="true"><g fill="#3fc1cf"><circle cx="4.5" cy="8.5" r="4.5"/><path d="M0.5 8 Q0.5 1 7.5 0 L7.5 2.2 Q3.5 3 3.5 7 Z"/><circle cx="15" cy="8.5" r="4.5"/><path d="M11 8 Q11 1 18 0 L18 2.2 Q14 3 14 7 Z"/></g></svg>For the law was given by Moses, but grace and truth came by Jesus Christ<svg class="quote-icon close" viewBox="0 0 20 13" aria-hidden="true"><g fill="#3fc1cf"><circle cx="4.5" cy="8.5" r="4.5"/><path d="M0.5 8 Q0.5 1 7.5 0 L7.5 2.2 Q3.5 3 3.5 7 Z"/><circle cx="15" cy="8.5" r="4.5"/><path d="M11 8 Q11 1 18 0 L18 2.2 Q14 3 14 7 Z"/></g></svg></p>
    <p class="citation">John 1:17</p>
  </section>

  <div class="hr" style="top:1103px"></div>

  <p class="summary">For these reasons, the distinction between the law and the gospel is the most heavily assaulted doctrine in the Christian faith. This Reformation Day, join us for an explanation and defense of the great distinction between God’s good law and God’s glorious gospel.</p>

  <p class="website">www.<span class="website-domain">brackenhollowchapel</span>.com</p>
</main>
</body>
</html>
```